Business Card Design for Lawn Management

Lawn Management

Industry/Entity Type

Business

Contact Information for Business Card

Calloway Lawn Management
Joel Calloway
Calloway_Lawn@brindlemail.com
404-555-0172

```html
<!DOCTYPE html>
<html lang="en">
<head>
<meta charset="utf-8">
<title>Calloway Lawn Management – Business Card</title>
<link rel="stylesheet" href="https://fonts.googleapis.com/css2?family=Open+Sans:wght@400;600&display=swap">
<style>
  :root {
    --backdrop: #e9e4dc;
    --card: #f7f7f7;
    --green-deep: #1f7a2e;
    --green-bright: #3fae45;
    --brand-green: #2a8a35;
    --swoosh-grey: #8a8a8e;
    --ink-white: #ffffff;
    --ink-muted: #555555;
  }
  * { margin: 0; padding: 0; box-sizing: border-box; }
  html, body { width: 1200px; height: 750px; overflow: hidden; }
  body {
    background: var(--backdrop);
    font-family: "Open Sans", Arial, sans-serif;
    position: relative;
  }
  .card {
    position: absolute;
    top: 252px;
    width: 492px;
    height: 281px;
    background: var(--card);
    overflow: hidden;
    box-shadow: 0 3px 8px rgba(0,0,0,0.25);
  }
  .card--front { left: 92px; }
  .card--back { left: 618px; }
  .card__art { position: absolute; inset: 0; width: 100%; height: 100%; }

  .wordmark {
    position: absolute;
    display: flex;
    align-items: center;
    gap: 10px;
    color: var(--brand-green);
    font-weight: 600;
  }
  .wordmark__dot {
    width: 22px; height: 22px; border-radius: 50%;
    background: var(--brand-green);
    flex: none;
  }
  .wordmark__name { line-height: 1.1; }
  .wordmark__primary { display: block; font-size: 26px; letter-spacing: 0.5px; }
  .wordmark__secondary { display: block; font-size: 14px; }
  .card--front .wordmark { left: 46px; top: 118px; }

  .contact {
    position: absolute;
    right: 33px;
    top: 156px;
    text-align: right;
    color: var(--ink-white);
  }
  .contact__name { font-size: 18px; font-weight: 600; }
  .contact__role { font-size: 13px; margin-top: 2px; }
  .contact__lines { margin-top: 22px; font-size: 12.5px; line-height: 19px; }
  .contact__line { display: flex; justify-content: flex-end; align-items: center; gap: 6px; }
  .contact__icon { width: 13px; height: 11px; flex: none; }

  .card--back .wordmark {
    right: 25px; top: 190px;
    text-align: right;
  }
  .card--back .wordmark__primary { font-size: 30px; }
  .card--back .wordmark__secondary { font-size: 16px; }
  .web {
    position: absolute;
    right: 27px;
    top: 252px;
    font-size: 11px;
    font-style: italic;
    letter-spacing: 2.5px;
    color: var(--ink-muted);
  }
</style>
</head>
<body>

<section class="card card--front" aria-label="Front of business card">
  <svg class="card__art" viewBox="0 0 525 300" preserveAspectRatio="none" aria-hidden="true">
    <defs>
      <linearGradient id="waveGreen" x1="0" y1="1" x2="1" y2="0">
        <stop offset="0" stop-color="#1f7a2e"/>
        <stop offset="0.5" stop-color="#3fae45"/>
        <stop offset="1" stop-color="#1f7a2e"/>
      </linearGradient>
    </defs>
    <path d="M0,214 C70,240 150,248 210,236 C150,252 70,250 0,232 Z" fill="var(--swoosh-grey)"/>
    <path d="M330,128 C380,85 440,70 525,72 L525,84 C450,82 390,95 330,128 Z" fill="var(--swoosh-grey)"/>
    <path d="M0,252 C110,290 250,275 330,170 C385,105 450,92 525,96 L525,300 L0,300 Z" fill="url(#waveGreen)"/>
  </svg>

  <div class="wordmark">
    <span class="wordmark__dot"></span>
    <span class="wordmark__name">
      <span class="wordmark__primary">CALLOWAY</span>
      <span class="wordmark__secondary">Lawn Management</span>
    </span>
  </div>

  <div class="contact">
    <p class="contact__name">Joel Calloway</p>
    <p class="contact__role">Director</p>
    <div class="contact__lines">
      <p class="contact__line">404-555-0172
        <svg class="contact__icon" viewBox="0 0 14 12" aria-hidden="true">
          <path d="M1,4 C1,1 13,1 13,4 L10,5 L9,3 L5,3 L4,5 Z M3,6 L11,6 L12,11 L2,11 Z" fill="#fff"/>
        </svg>
      </p>
      <p class="contact__line">Calloway_Lawn@brindlemail.com
        <svg class="contact__icon" viewBox="0 0 14 12" aria-hidden="true">
          <rect x="1" y="2" width="12" height="8" fill="#fff"/>
          <path d="M1,2 L7,7 L13,2" fill="none" stroke="#1f7a2e" stroke-width="1.2"/>
        </svg>
      </p>
    </div>
  </div>
</section>

<section class="card card--back" aria-label="Back of business card">
  <svg class="card__art" viewBox="0 0 525 300" preserveAspectRatio="none" aria-hidden="true">
    <defs>
      <radialGradient id="backGreen" cx="0.4" cy="0.4" r="0.7">
        <stop offset="0" stop-color="#3fae45"/>
        <stop offset="1" stop-color="#23843a"/>
      </radialGradient>
    </defs>
    <circle cx="120" cy="140" r="170" fill="url(#backGreen)"/>
  </svg>

  <div class="wordmark">
    <span class="wordmark__name">
      <span class="wordmark__primary">CALLOWAY</span>
      <span class="wordmark__secondary">Lawn Management</span>
    </span>
  </div>
  <p class="web">www.callowaylawncare.com</p>
</section>

</body>
</html>
```